Design Cloud for Core Values & Attributes

See Image Example Below "Word Cloud" this is what we would like this to look like.
The second image is all of the Core Value and Attributes I will list below.
CORE VALUES need to be the bigger words (based off the image I sent) Capitalized, BOLD, Navy
Independence, Capitalism, Trust, Fun, Safety, Growth
ATTRIBUTES need to be the smaller words, lower case, non-bold, lighter blue mixed in (based off the image I sent):
Humility, Consistency, Open Mindedness, Curiosity, Selflessness, Caring, Conscientiousness, Honorable, Cunning, Competitive, Compartmentalization, Innovative, Perseverance, Authenticity, Decisiveness, Self-efficacy, Accountability, Generosity, Humor, Optimism, Resilience, Inclusive, Insouciance to what others think, Courage, Decisive, Curious, Integrity

```html
<!DOCTYPE html>
<html lang="en">
<head>
<meta charset="utf-8">
<title>Core Values &amp; Attributes Word Cloud</title>
<link rel="stylesheet" href="https://fonts.googleapis.com/css2?family=Fira+Sans+Condensed:wght@400;800&display=swap">
<style>
  :root {
    --core-blue: #2b83ee;
    --attr-cyan: #33ebf3;
    --attr-pale: #82f3f8;
    --accent-yellow: #ffe100;
    --bg: #ffffff;
  }
  html, body {
    margin: 0;
    padding: 0;
    overflow: hidden;
    background: var(--bg);
  }
  .cloud {
    position: relative;
    width: 1200px;
    height: 1000px;
    overflow: hidden;
    background: var(--bg);
    font-family: "Fira Sans Condensed", "Arial Narrow", sans-serif;
  }
  .word {
    position: absolute;
    margin: 0;
    line-height: 1;
    white-space: nowrap;
    font-weight: 400;
  }
  .core { color: var(--core-blue); font-weight: 800; text-transform: uppercase; letter-spacing: -0.01em; }
  .attr { color: var(--attr-cyan); }
  .attr-pale { color: var(--attr-pale); }
  .feature { color: var(--accent-yellow); }
  .vertical {
    writing-mode: vertical-rl;
    transform: rotate(180deg);
  }
</style>
</head>
<body>
<main class="cloud" aria-label="Core values and attributes word cloud">
  <!-- upper centre cluster -->
  <span class="word attr" style="left:503px;top:204px;font-size:27px">humility</span>
  <span class="word attr" style="left:472px;top:255px;font-size:37px">curiosity</span>
  <span class="word attr" style="left:429px;top:313px;font-size:34px">selflessness</span>
  <span class="word attr" style="left:371px;top:361px;font-size:36px">conscientiousness</span>
  <span class="word attr vertical" style="left:612px;top:189px;font-size:32px">consistency</span>
  <span class="word attr-pale vertical" style="left:657px;top:183px;font-size:37px">conscientiousness</span>
  <span class="word attr-pale" style="left:701px;top:196px;font-size:27px">cunning</span>
  <span class="word attr-pale" style="left:701px;top:259px;font-size:29px">honorable</span>
  <span class="word attr-pale" style="left:701px;top:298px;font-size:43px">innovative</span>

  <!-- left cluster -->
  <span class="word attr-pale" style="left:213px;top:293px;font-size:26px">curious</span>
  <span class="word attr-pale" style="left:197px;top:340px;font-size:27px">decisive</span>
  <span class="word attr-pale" style="left:177px;top:374px;font-size:34px">integrity</span>
  <span class="word attr-pale vertical" style="left:293px;top:298px;font-size:32px">courage</span>
  <span class="word attr-pale vertical" style="left:344px;top:347px;font-size:19px">caring</span>
  <span class="word attr-pale" style="left:89px;top:421px;font-size:41px">accountability</span>
  <span class="word attr-pale" style="left:55px;top:497px;font-size:27px">humility</span>
  <span class="word core" style="left:146px;top:478px;font-size:49px">Safety</span>
  <span class="word attr-pale vertical" style="left:301px;top:478px;font-size:19px">caring</span>

  <!-- centre -->
  <span class="word core" style="left:337px;top:406px;font-size:61px">Trust</span>
  <span class="word feature" style="left:519px;top:404px;font-size:58px">open</span>
  <span class="word feature" style="left:338px;top:466px;font-size:60px">mindedness</span>
  <span class="word attr" style="left:258px;top:548px;font-size:39px">innovative</span>
  <span class="word core" style="left:444px;top:540px;font-size:48px">Growth</span>

  <!-- right of centre -->
  <span class="word attr-pale" style="left:763px;top:357px;font-size:34px">competitive</span>
  <span class="word attr-pale" style="left:718px;top:400px;font-size:37px">perseverance</span>
  <span class="word core" style="left:693px;top:442px;font-size:49px">Capitalism</span>
  <span class="word attr-pale" style="left:659px;top:497px;font-size:31px">compartmentalization</span>
  <span class="word attr-pale" style="left:631px;top:563px;font-size:26px">cunning</span>
  <span class="word feature" style="left:728px;top:541px;font-size:63px">humility</span>

  <!-- far right -->
  <span class="word attr" style="left:939px;top:355px;font-size:26px">humility</span>
  <span class="word attr" style="left:939px;top:391px;font-size:36px">optimism</span>
  <span class="word attr" style="left:939px;top:434px;font-size:39px">humor</span>
  <span class="word attr" style="left:1051px;top:435px;font-size:29px">inclusive</span>
  <span class="word attr vertical" style="left:942px;top:485px;font-size:20px">caring</span>
  <span class="word core" style="left:975px;top:480px;font-size:56px">Fun</span>
  <span class="word attr" style="left:1006px;top:544px;font-size:29px">resilience</span>
  <span class="word attr vertical" style="left:935px;top:553px;font-size:29px">insouciance</span>
  <span class="word attr vertical" style="left:969px;top:553px;font-size:29px">to what others think</span>

  <!-- lower cluster -->
  <span class="word attr" style="left:283px;top:614px;font-size:27px">humility</span>
  <span class="word attr" style="left:376px;top:599px;font-size:39px">curiosity</span>
  <span class="word attr" style="left:326px;top:656px;font-size:34px">accountability</span>
  <span class="word attr" style="left:355px;top:707px;font-size:36px">generosity</span>
  <span class="word attr" style="left:459px;top:772px;font-size:29px">honorable</span>
  <span class="word feature vertical" style="left:531px;top:595px;font-size:54px">caring</span>
  <span class="word attr vertical" style="left:585px;top:629px;font-size:32px">perseverance</span>
  <span class="word core" style="left:631px;top:619px;font-size:49px">Independence</span>
  <span class="word attr-pale" style="left:631px;top:684px;font-size:27px">curiosity</span>
  <span class="word attr" style="left:750px;top:678px;font-size:36px">self-efficacy</span>
  <span class="word attr-pale" style="left:631px;top:721px;font-size:36px">authenticity</span>
  <span class="word attr-pale" style="left:810px;top:729px;font-size:29px">decisiveness</span>
  <span class="word attr-pale" style="left:751px;top:772px;font-size:22px">selflessness</span>
</main>
</body>
</html>
```